Lanternleaf - Fresh Asian Cuisine Menu

We need to redo our menu to include pictures of food items. Our restaurant is vibrant, trendy, upscale Chinese cuisine

Requirements
Must have
• Must fit on 8.5x11 paper. We can remove the About Us section if needed but menu cannot be more than 6 pages total. Must include pictures of menu items

```html
<!DOCTYPE html>
<html lang="en">
<head>
<meta charset="utf-8">
<title>Lanternleaf - Fresh Asian Cuisine — Entrees</title>
<link rel="stylesheet" href="https://fonts.googleapis.com/css2?family=Alegreya+Sans+SC:wght@700&family=Fira+Sans+Condensed:wght@300;600;700;800&family=Passion+One:wght@700&display=swap">
<style>
  :root {
    --page-bg: #1e1e20;
    --brand-red: #e3131b;
    --title-bar: #6a1210;
    --title-text: #f4ead8;
    --section-green: #6fb246;
    --body-text: #ececec;
    --white: #ffffff;
  }
  * { box-sizing: border-box; margin: 0; padding: 0; }
  html, body { width: 927px; height: 1200px; overflow: hidden; background: var(--page-bg); }
  .menu-page { position: relative; width: 927px; height: 1200px; background: var(--page-bg); font-family: "Fira Sans Condensed", sans-serif; }

  .rule { position: absolute; height: 8px; background: var(--brand-red); }

  .page-title {
    position: absolute; left: 250px; top: 20px; width: 210px; text-align: center;
    font-family: "Passion One", sans-serif; font-size: 46px; line-height: 1; letter-spacing: 1px;
    color: var(--brand-red); -webkit-text-stroke: 1.5px var(--white);
  }

  .brand { position: absolute; display: flex; flex-direction: column; align-items: flex-end; color: var(--white); font-family: "Fira Sans Condensed", sans-serif; font-weight: 800; }
  .brand-name { font-size: 31px; line-height: 1; letter-spacing: 0.5px; text-transform: uppercase; }
  .brand-tagline { font-size: 9px; letter-spacing: 1.6px; text-transform: uppercase; margin-top: 2px; }
  .brand--top { left: 688px; top: 30px; width: 204px; }
  .brand--bottom { left: 48px; top: 1150px; width: 204px; }

  .section-heading {
    position: absolute; top: 86px; width: 424px; text-align: center;
    font-weight: 700; font-size: 28px; color: var(--section-green); letter-spacing: 0.3px;
  }

  .menu-column { position: absolute; top: 132px; width: 424px; display: flex; flex-direction: column; gap: 15px; }
  .menu-column--left { left: 26px; }
  .menu-column--right { left: 476px; }

  .dish { position: relative; height: 187px; }
  .dish-name {
    height: 25px; background: var(--title-bar); color: var(--title-text); text-align: center;
    font-family: "Alegreya Sans SC", sans-serif; font-weight: 700; font-size: 21px; line-height: 25px; letter-spacing: 0.5px;
  }
  .dish-body { display: flex; height: 162px; }
  .dish-photo { position: relative; width: 231px; height: 162px; flex: none; }
  .dish-desc {
    flex: 1; display: flex; align-items: center; padding-left: 9px;
    font-weight: 300; font-size: 16.5px; line-height: 22px; color: var(--body-text);
  }
  .price {
    position: absolute; left: 1px; top: 30px; width: 76px; height: 76px; border-radius: 50%;
    background: var(--brand-red); color: var(--white); display: flex; align-items: center; justify-content: center;
    font-weight: 600; font-size: 37px; letter-spacing: -0.5px;
  }
  .heat { position: absolute; left: 0; bottom: 0; display: flex; flex-direction: column; gap: 1px; }
  .heat svg { display: block; width: 30px; height: 24px; }

  .tone-duck { background: linear-gradient(135deg, #5c6070, #b7a99b 45%, #8c4a2c); }
  .tone-lamb { background: linear-gradient(135deg, #7a6a5c, #d8cfc2 40%, #7a3a1e 70%, #5d5a4a); }
  .tone-fish { background: radial-gradient(circle at 55% 50%, #c0401a 0%, #a52b12 45%, #e9e2d8 70%, #8c8a8e); }
  .tone-scallop { background: radial-gradient(circle at 55% 40%, #4a2514 0%, #3a6d2a 40%, #eeeae4 68%, #8a8892); }
  .tone-spicybeef { background: radial-gradient(circle at 45% 50%, #6a2a12 0%, #a1381a 35%, #e9e3db 55%, #2a2a2e); }
  .tone-dancing { background: radial-gradient(circle at 50% 50%, #9c5a28 0%, #6a2a14 30%, #f0ece6 60%, #6e6a66); }
  .tone-oyster { background: radial-gradient(circle at 50% 50%, #3b2416 0%, #4a2c1a 30%, #f2efea 60%, #8e8b8c); }
  .tone-double { background: radial-gradient(circle at 50% 50%, #8a1c10 0%, #a52812 35%, #e8e2da 65%, #7d7875); }
  .tone-blackpepper { background: radial-gradient(circle at 50% 50%, #3d2c22 0%, #5a4a3c 40%, #2d2d2f 75%, #4a4a4c); }
  .tone-ribs { background: radial-gradient(circle at 48% 48%, #3a1c0e 0%, #5a2c12 30%, #f2efe9 58%, #3a3a3e); }
</style>
</head>
<body>
<main class="menu-page">
  <div class="rule" style="left:0; top:42px; width:250px;"></div>
  <div class="rule" style="left:460px; top:42px; width:222px;"></div>
  <div class="rule" style="left:898px; top:42px; width:29px;"></div>
  <h1 class="page-title">ENTREES</h1>
  <div class="brand brand--top"><span class="brand-name">Lanternleaf</span><span class="brand-tagline">Fresh Asian Cuisine</span></div>

  <h2 class="section-heading" style="left:26px;">CHEF SPECIALTIES</h2>
  <h2 class="section-heading" style="left:476px;">BEEF &amp; PORK</h2>

  <section class="menu-column menu-column--left">
    <article class="dish">
      <h3 class="dish-name">Jasmine Tea Smoked Duck</h3>
      <div class="dish-body">
        <div class="dish-photo tone-duck" role="img" aria-label="Photo of sliced smoked duck with steamed buns and sauce">
          <span class="price">$24</span>
        </div>
        <p class="dish-desc">Boneless half duck served with thinly sliced cucumber, scallion, house made duck sauce and soft flour wrap</p>
      </div>
    </article>
    <article class="dish">
      <h3 class="dish-name">Sizzling Cumin’ Lamb</h3>
      <div class="dish-body">
        <div class="dish-photo tone-lamb" role="img" aria-label="Photo of cumin lamb with peppers and onions">
          <span class="price">$16</span>
          <div class="heat"><svg viewBox="0 0 30 24"><rect width="30" height="24" fill="#fff"/><path d="M5 20c8 1 16-4 19-13 1-2 3-3 4-2-1 1-1 2-2 3-3 9-12 14-21 12z" fill="#e3131b"/></svg></div>
        </div>
        <p class="dish-desc">Tender pieces of lamb rubbed in cumin, Sichuan peppers, red and green bell peppers and onions</p>
      </div>
    </article>
    <article class="dish">
      <h3 class="dish-name">Chef Lin’s Spicy Fish</h3>
      <div class="dish-body">
        <div class="dish-photo tone-fish" role="img" aria-label="Photo of spicy fish filet in red chili broth with cilantro">
          <span class="price">$17</span>
          <div class="heat"><svg viewBox="0 0 30 24"><rect width="30" height="24" fill="#fff"/><path d="M5 20c8 1 16-4 19-13 1-2 3-3 4-2-1 1-1 2-2 3-3 9-12 14-21 12z" fill="#e3131b"/></svg></div>
        </div>
        <p class="dish-desc">Fish filet in house made green peppercorn sauce with Chinese cabbage, sprouts and celery garnished with fresh Sichuan peppercorn, Thai chili and cilantro</p>
      </div>
    </article>
    <article class="dish">
      <h3 class="dish-name">General Tso’s Scallops</h3>
      <div class="dish-body">
        <div class="dish-photo tone-scallop" role="img" aria-label="Photo of glazed scallops with broccoli">
          <span class="price">$18</span>
          <div class="heat"><svg viewBox="0 0 30 24"><rect width="30" height="24" fill="#fff"/><path d="M5 20c8 1 16-4 19-13 1-2 3-3 4-2-1 1-1 2-2 3-3 9-12 14-21 12z" fill="#e3131b"/></svg><svg viewBox="0 0 30 24"><rect width="30" height="24" fill="#fff"/><path d="M5 20c8 1 16-4 19-13 1-2 3-3 4-2-1 1-1 2-2 3-3 9-12 14-21 12z" fill="#e3131b"/></svg></div>
        </div>
        <p class="dish-desc">The perfect combination of tender scallops marinated in a sweet chili sauce with broccoli and red peppers</p>
      </div>
    </article>
    <article class="dish">
      <h3 class="dish-name">Chef Lin’s Spicy Beef</h3>
      <div class="dish-body">
        <div class="dish-photo tone-spicybeef" role="img" aria-label="Photo of spicy beef in chili sauce">
          <span class="price">$16</span>
          <div class="heat"><svg viewBox="0 0 30 24"><rect width="30" height="24" fill="#fff"/><path d="M5 20c8 1 16-4 19-13 1-2 3-3 4-2-1 1-1 2-2 3-3 9-12 14-21 12z" fill="#e3131b"/></svg><svg viewBox="0 0 30 24"><rect width="30" height="24" fill="#fff"/><path d="M5 20c8 1 16-4 19-13 1-2 3-3 4-2-1 1-1 2-2 3-3 9-12 14-21 12z" fill="#e3131b"/></svg></div>
        </div>
        <p class="dish-desc">Angus beef in house made green peppercorn sauce with Chinese cabbage, sprouts and celery garnished with fresh Sichuan peppercorn, Thai chili and cilantro</p>
      </div>
    </article>
  </section>

  <section class="menu-column menu-column--right">
    <article class="dish">
      <h3 class="dish-name">Dancing Beef</h3>
      <div class="dish-body">
        <div class="dish-photo tone-dancing" role="img" aria-label="Photo of beef slices over sizzling rice crackers">
          <span class="price">$16</span>
          <div class="heat"><svg viewBox="0 0 30 24"><rect width="30" height="24" fill="#fff"/><path d="M5 20c8 1 16-4 19-13 1-2 3-3 4-2-1 1-1 2-2 3-3 9-12 14-21 12z" fill="#e3131b"/></svg><svg viewBox="0 0 30 24"><rect width="30" height="24" fill="#fff"/><path d="M5 20c8 1 16-4 19-13 1-2 3-3 4-2-1 1-1 2-2 3-3 9-12 14-21 12z" fill="#e3131b"/></svg><svg viewBox="0 0 30 24"><rect width="30" height="24" fill="#fff"/><path d="M5 20c8 1 16-4 19-13 1-2 3-3 4-2-1 1-1 2-2 3-3 9-12 14-21 12z" fill="#e3131b"/></svg></div>
        </div>
        <p class="dish-desc">Angus Beef slices on a bed of sizzling rice crackers, black peppercorn and Thai chili</p>
      </div>
    </article>
    <article class="dish">
      <h3 class="dish-name">Oyster Beef</h3>
      <div class="dish-body">
        <div class="dish-photo tone-oyster" role="img" aria-label="Photo of wok fried steak in oyster sauce">
          <span class="price">$14</span>
        </div>
        <p class="dish-desc">Tender cuts of steak wok fried with onions and marinated in a homemade oyster sauce</p>
      </div>
    </article>
    <article class="dish">
      <h3 class="dish-name">Double Pepper Beef</h3>
      <div class="dish-body">
        <div class="dish-photo tone-double" role="img" aria-label="Photo of steak with chilies and peppers in red sauce">
          <span class="price">$16</span>
          <div class="heat"><svg viewBox="0 0 30 24"><rect width="30" height="24" fill="#fff"/><path d="M5 20c8 1 16-4 19-13 1-2 3-3 4-2-1 1-1 2-2 3-3 9-12 14-21 12z" fill="#e3131b"/></svg><svg viewBox="0 0 30 24"><rect width="30" height="24" fill="#fff"/><path d="M5 20c8 1 16-4 19-13 1-2 3-3 4-2-1 1-1 2-2 3-3 9-12 14-21 12z" fill="#e3131b"/></svg><svg viewBox="0 0 30 24"><rect width="30" height="24" fill="#fff"/><path d="M5 20c8 1 16-4 19-13 1-2 3-3 4-2-1 1-1 2-2 3-3 9-12 14-21 12z" fill="#e3131b"/></svg></div>
        </div>
        <p class="dish-desc">Angus steak with peppercorn, Thai chili, Serrano pepper and tofu and rice noodles</p>
      </div>
    </article>
    <article class="dish">
      <h3 class="dish-name">Black Pepper Steak</h3>
      <div class="dish-body">
        <div class="dish-photo tone-blackpepper" role="img" aria-label="Photo of steak with onions and bell peppers in a pan">
          <span class="price">$15</span>
          <div class="heat"><svg viewBox="0 0 30 24"><rect width="30" height="24" fill="#fff"/><path d="M5 20c8 1 16-4 19-13 1-2 3-3 4-2-1 1-1 2-2 3-3 9-12 14-21 12z" fill="#e3131b"/></svg></div>
        </div>
        <p class="dish-desc">Tender cuts of steak mixed with onions and red and green bell peppers</p>
      </div>
    </article>
    <article class="dish">
      <h3 class="dish-name">Singapore Baby Back Ribs</h3>
      <div class="dish-body">
        <div class="dish-photo tone-ribs" role="img" aria-label="Photo of glazed baby back ribs with bok choy">
          <span class="price">$16</span>
        </div>
        <p class="dish-desc">Tender Baby back ribs rubbed in a Thai inspired sweet tangy glaze</p>
      </div>
    </article>
  </section>

  <div class="rule" style="left:0; top:1162px; width:40px;"></div>
  <div class="rule" style="left:262px; top:1162px; width:665px;"></div>
  <div class="brand brand--bottom"><span class="brand-name">Lanternleaf</span><span class="brand-tagline">Fresh Asian Cuisine</span></div>
</main>
</body>
</html>
```